Packaging Design for Dates Products Exports

We are exporters of Dates products globally - company name is Crescent Meadow Provisions LLC.

We are looking to revamp our boxes packaging - I have attached our preliminary logo.

Our color palette is predominantly dark green and gold. Packaging can include shades of black, dark red, beige - I have included another very preliminary sample for clarity.

Note please we are looking for substantially better designs than both attached pictures. Our products are of premium quality and would want our packaging to reflect that. Please be inspired by Dates products packaging of global suppliers as well to get a sense of industry-specific themes.

Packaging size is 430mm length, 150mm width, 280mm height.

Target Market(s)

Dates products wholesale importers in Asia, Europe, US, Australia, etx

Industry/Entity Type

Dates Products

Font styles to use
Decorative
Script

Colors

Designer to choose colors to be used in the design.

Requirements
Must have
• Premium look and feel reflecting product quality, company & industry-specific color palette/design themes that are relevant

```html
<!DOCTYPE html>
<html lang="en">
<head>
<meta charset="utf-8">
<title>Crescent Meadow Provisions – Premium Dates Box Panels</title>
<link href="https://fonts.googleapis.com/css2?family=Cinzel:wght@400;600&family=Pinyon+Script&family=Montserrat:wght@400;600;700&display=swap" rel="stylesheet">
<style>
  :root {
    --stage: #d9d9d9;
    --green-deep: #0f4a2c;
    --green-mid: #1a5a37;
    --green-side: #0d4127;
    --gold-light: #f3d98a;
    --gold: #c9a13b;
    --gold-dark: #8a6418;
    --ivory: #f1efe8;
    --label-white: #ffffff;
    --ink: #1b1b1b;
    --copper: #c9824d;
    --date-brown: #5e1a10;
    --badge-green: #1f9a4d;
  }
  * { box-sizing: border-box; margin: 0; padding: 0; }
  html, body {
    width: 1200px; height: 857px; overflow: hidden;
    background: var(--stage);
  }
  .canvas {
    position: relative; width: 1200px; height: 857px;
    display: flex; align-items: center; justify-content: center;
  }
  .box-net { display: flex; }

  /* ---------- Side panel ---------- */
  .side-panel {
    position: relative; width: 180px; height: 790px;
    background: linear-gradient(180deg, var(--green-mid), var(--green-side));
    overflow: hidden;
  }
  .ornament-strip {
    position: absolute; top: 14px; bottom: 14px; width: 22px;
    background: linear-gradient(180deg, var(--gold-dark), var(--gold), var(--gold-dark));
    opacity: .45; border-radius: 3px;
  }
  .ornament-strip--left { left: 8px; }
  .ornament-strip--right { right: 8px; }
  .nutrition-label {
    position: absolute; top: 70px; left: 40px; right: 40px;
    background: var(--label-white); color: var(--ink);
    border: 2px solid var(--ink);
    padding: 6px 6px 8px;
    font-family: "Montserrat", sans-serif;
  }
  .nutrition-label__title {
    font-weight: 700; font-size: 12px; line-height: 1.1;
    border-bottom: 4px solid var(--ink); padding-bottom: 3px;
  }
  .nutrition-label__serving {
    font-size: 8px; padding: 3px 0; border-bottom: 2px solid var(--ink);
  }
  .nutrition-label__row {
    display: flex; justify-content: space-between;
    font-size: 8px; line-height: 1.9;
    border-bottom: 1px solid #888;
  }
  .nutrition-label__row:last-child { border-bottom: 3px solid var(--ink); }
  .cert-badges {
    position: absolute; top: 470px; left: 40px; right: 40px;
    display: flex; flex-direction: column; align-items: center; gap: 22px;
  }
  .cert-badge {
    width: 52px; height: 52px; border-radius: 50%;
    border: 2px solid var(--gold); opacity: .7;
  }
  .handling-icons {
    position: absolute; bottom: 60px; left: 40px; right: 40px;
    display: flex; justify-content: space-between;
  }
  .handling-icon {
    width: 16px; height: 16px;
    border: 1.5px solid var(--ivory); opacity: .75;
  }

  /* ---------- Front panel ---------- */
  .front-panel {
    position: relative; width: 520px; height: 790px;
    background: radial-gradient(ellipse at 50% 45%, var(--green-mid) 0%, var(--green-deep) 80%);
    overflow: hidden;
  }
  .ornament-band {
    position: absolute; left: 14px; right: 14px; height: 58px;
    background: linear-gradient(90deg, var(--gold-dark), var(--gold), var(--gold-light), var(--gold), var(--gold-dark));
    opacity: .45; border-radius: 4px;
  }
  .ornament-band--top { top: 14px; }
  .ornament-band--bottom { bottom: 14px; }

  .brand-lockup {
    position: absolute; top: 112px; left: 0; right: 0;
    display: flex; flex-direction: column; align-items: center; gap: 14px;
  }
  .brand-dot {
    width: 64px; height: 64px; border-radius: 50%;
    border: 3px solid var(--ivory);
  }
  .brand-name {
    font-family: "Cinzel", serif; font-weight: 400;
    color: var(--ivory); text-align: center;
    font-size: 27px; line-height: 1.15; letter-spacing: .5px;
  }
  .brand-name span { display: block; font-size: 15px; letter-spacing: 1.5px; }

  .product-title {
    position: absolute; top: 318px; left: 0; right: 0; text-align: center;
  }
  .product-title__eyebrow {
    font-family: "Cinzel", serif; font-weight: 400;
    font-size: 22px; letter-spacing: 6px; color: var(--ivory);
    padding-left: 70px;
  }
  .product-title__name {
    font-family: "Pinyon Script", cursive; font-weight: 400;
    font-size: 104px; line-height: .95;
    background: linear-gradient(180deg, var(--gold-light) 0%, var(--gold) 55%, var(--gold-dark) 100%);
    -webkit-background-clip: text; background-clip: text; color: transparent;
  }

  .product-visual {
    position: absolute; top: 478px; left: 125px; width: 240px; height: 180px;
    border-radius: 8px;
    background: linear-gradient(180deg, var(--date-brown) 0%, var(--copper) 100%);
    opacity: .85;
  }
  .quality-seal {
    position: absolute; top: 570px; left: 372px;
    width: 86px; height: 86px; border-radius: 50%;
    background: radial-gradient(circle, var(--gold-light) 0%, var(--gold) 60%, var(--gold-dark) 100%);
    border: 3px solid var(--gold-dark);
  }
  .net-weight {
    position: absolute; top: 676px; left: 50%; transform: translateX(-50%);
    font-family: "Montserrat", sans-serif; font-weight: 600;
    font-size: 14px; color: #0b2a17;
    background: var(--badge-green);
    padding: 4px 14px; border-radius: 12px;
  }
</style>
</head>
<body>
<main class="canvas">
  <div class="box-net">
    <aside class="side-panel">
      <div class="ornament-strip ornament-strip--left" role="img" aria-label="Gold arabesque ornament strip"></div>
      <div class="ornament-strip ornament-strip--right" role="img" aria-label="Gold arabesque ornament strip"></div>

      <div class="nutrition-label">
        <p class="nutrition-label__title">Nutrition Facts</p>
        <p class="nutrition-label__serving">Serving Size 40g</p>
        <p class="nutrition-label__row"><span>Calories</span><span>110</span></p>
        <p class="nutrition-label__row"><span>Total Fat</span><span>0g</span></p>
        <p class="nutrition-label__row"><span>Sodium</span><span>0mg</span></p>
        <p class="nutrition-label__row"><span>Carbohydrate</span><span>30g</span></p>
        <p class="nutrition-label__row"><span>Dietary Fiber</span><span>3g</span></p>
        <p class="nutrition-label__row"><span>Sugars</span><span>25g</span></p>
        <p class="nutrition-label__row"><span>Protein</span><span>1g</span></p>
      </div>

      <div class="cert-badges">
        <div class="cert-badge"></div>
        <div class="cert-badge"></div>
        <div class="cert-badge"></div>
      </div>

      <div class="handling-icons">
        <span class="handling-icon"></span>
        <span class="handling-icon"></span>
        <span class="handling-icon"></span>
        <span class="handling-icon"></span>
        <span class="handling-icon"></span>
      </div>
    </aside>

    <section class="front-panel">
      <div class="ornament-band ornament-band--top" role="img" aria-label="Gold arabesque ornament border"></div>

      <div class="brand-lockup">
        <div class="brand-dot"></div>
        <p class="brand-name">CRESCENT MEADOW<span>PROVISIONS LLC</span></p>
      </div>

      <div class="product-title">
        <p class="product-title__eyebrow">PREMIUM</p>
        <h1 class="product-title__name">Dates</h1>
      </div>

      <div class="product-visual" role="img" aria-label="Illustration of a copper bowl filled with glossy dark dates"></div>
      <div class="quality-seal"></div>

      <p class="net-weight">5Kg</p>

      <div class="ornament-band ornament-band--bottom" role="img" aria-label="Gold arabesque ornament border"></div>
    </section>
  </div>
</main>
</body>
</html>
```